A5 5mm Grid and Dot Grid Page Layout

I need 2 designs:
1] A5 (5.75" x 8" inches final trimmed page size ) 128 journal pages with a 5mm x 5mm grid layout
2} A5 (5.75" x 8" inches final trimmed page size) 128 journal pages with 5mm x 5mm dot grid layout
First and last page should be blank
grid and dot grid should be a light gray color
Final design should you in PDF format

Target Market(s)

Fountain Pen Notebooks

Industry/Entity Type

Notebooks and Journals

Colors

Designer to choose only greyscale colors for use in the design.

Requirements
Must have
• Light gray 5mm x 5mm grid and dot grid page layout. Very thin lines
Should not have
• Thick black grid or dots

```html
<!DOCTYPE html>
<html lang="en">
<head>
<meta charset="utf-8">
<title>A5 5mm Grid Journal Page</title>
<style>
  :root {
    --page-bg: #ffffff;
    --grid-line: #bdbdbd;
    --cell: 29px;
  }
  html, body {
    margin: 0;
    padding: 0;
    width: 861px;
    height: 1200px;
    overflow: hidden;
    background: var(--page-bg);
  }
  .journal-page {
    position: relative;
    width: 861px;
    height: 1200px;
    background: var(--page-bg);
  }
  .grid-area {
    position: absolute;
    left: 33px;
    top: 29px;
    width: calc(var(--cell) * 27);
    height: calc(var(--cell) * 39);
    box-sizing: content-box;
    border-right: 1px solid var(--grid-line);
    border-bottom: 1px solid var(--grid-line);
    background-image:
      linear-gradient(to right, var(--grid-line) 1px, transparent 1px),
      linear-gradient(to bottom, var(--grid-line) 1px, transparent 1px);
    background-size: var(--cell) var(--cell);
    background-position: 0 0;
  }
</style>
</head>
<body>
  <main class="journal-page">
    <div class="grid-area"></div>
  </main>
</body>
</html>
```